Business Card Design

We need a new business card design for a company based in Alderwood, NM. We provide business consulting services in the information technology / services space. We like variations of the color blue, aqua, black, light tan, and white. Would like "cool" tones. The design should clearly communicate professionalism. Think outside the box - we don't want something "typical". Our company name is "Harlow Advisory, LLC".
Updates

Thank you all for your submissions. We have seen some very creative and inspired designs. We have made a decision and will be moving forward with that design. Appreciate all of the hard work.

Industry/Entity Type

Information Technology

Contact Information for Business Card

Megan Harlow Pruett
318 West Birchfield Run Dr.
Alderwood, NM 76418

```html
<!DOCTYPE html>
<html lang="en">
<head>
<meta charset="utf-8">
<title>Harlow Advisory — Business Card</title>
<link rel="stylesheet" href="https://fonts.googleapis.com/css2?family=Montserrat:wght@400;500;600&display=swap">
<style>
  :root {
    --page-bg: #e6e8ea;
    --card-white: #ffffff;
    --card-white-shade: #eef0f1;
    --teal-light: #2aa6b4;
    --teal-mid: #1b8d9c;
    --teal-deep: #15606c;
    --ink: #1c1c1c;
    --ink-soft: #4a4a4a;
    --logo-text: #ffffff;
  }
  * { margin: 0; padding: 0; box-sizing: border-box; }
  html, body {
    width: 1200px;
    height: 900px;
    overflow: hidden;
    background: var(--page-bg);
    font-family: "Montserrat", Arial, sans-serif;
  }
  .stage {
    width: 1200px;
    height: 900px;
    display: flex;
    align-items: center;
    justify-content: center;
  }
  .business-card {
    position: relative;
    width: 840px;
    height: 480px;
    background: linear-gradient(135deg, var(--card-white) 0%, var(--card-white-shade) 100%);
    box-shadow: 0 10px 30px rgba(0, 0, 0, 0.18);
    overflow: hidden;
  }
  .brand-panel {
    position: absolute;
    inset: 0;
    background: radial-gradient(ellipse at 55% 30%, var(--teal-light) 0%, var(--teal-mid) 45%, var(--teal-deep) 100%);
    clip-path: polygon(32% 0, 100% 0, 100% 100%, 59% 100%);
  }
  .brand-lockup {
    position: absolute;
    left: 54%;
    top: 38%;
    display: flex;
    align-items: center;
    gap: 18px;
  }
  .brand-dot {
    width: 64px;
    height: 64px;
    border-radius: 50%;
    background: var(--logo-text);
  }
  .brand-name {
    color: var(--logo-text);
    font-size: 30px;
    font-weight: 600;
    letter-spacing: 0.2px;
  }
  .contact-block {
    position: absolute;
    left: 12%;
    top: 66%;
  }
  .contact-name {
    color: var(--ink);
    font-size: 25px;
    font-weight: 600;
    margin-bottom: 16px;
  }
  .contact-company {
    color: var(--ink-soft);
    font-size: 19px;
    font-weight: 400;
    margin-left: 34px;
    margin-bottom: 6px;
  }
  .contact-address {
    color: var(--ink-soft);
    font-size: 13px;
    font-weight: 500;
    font-style: italic;
    margin-left: 34px;
    white-space: nowrap;
  }
</style>
</head>
<body>
  <main class="stage">
    <article class="business-card">
      <div class="brand-panel"></div>
      <div class="brand-lockup">
        <span class="brand-dot"></span>
        <span class="brand-name">Harlow Advisory</span>
      </div>
      <div class="contact-block">
        <p class="contact-name">Megan Harlow Pruett</p>
        <p class="contact-company">Harlow Advisory, LLC</p>
        <p class="contact-address">318 West Birchfield Run Dr. Alderwood, NM 76418</p>
      </div>
    </article>
  </main>
</body>
</html>
```